Bride Basecamp

I am looking for a design for http://www.bridebasecamp.co.uk/ its a joomla site and I am going to set up with the same mods as our stag version http://www.groomsnightout.co.uk/ you will see on groomsnight how all the menus look and are positioned. Here is an example of a activity page http://www.groomsnightout.co.uk/activity/white-water-rafting-in-perthshire.html which comes from Kiva.

The design needs to be built for responsive layout. The brand look and feel needs to be 100% for the female market.

We can accept the design in photoshop or something similar

Please ask questions if you require more information.

some examples of hen sites

http://www.girlsgetaway.co.uk/

```html
<!DOCTYPE html>
<html lang="en">
<head>
<meta charset="utf-8">
<title>Bride Basecamp</title>
<link rel="stylesheet" href="https://fonts.googleapis.com/css2?family=Libre+Baskerville:wght@700&family=Open+Sans:wght@300;400;600&display=swap">
<style>
:root{
  --band-top:#d4504f;
  --band-bottom:#b93a40;
  --nav:#e56a5f;
  --nav-line:#f08a7f;
  --accent:#c24a46;
  --ink:#222;
  --muted:#777;
  --rule:#e4e4e4;
  --card:#f3f3f3;
  --footer:#262626;
  --footer-line:#e0574f;
  --star:#f4b400;
}
*{box-sizing:border-box;margin:0;padding:0}
html,body{width:754px;height:1200px;overflow:hidden;background:#fff}
body{position:relative;font-family:"Open Sans",sans-serif;color:var(--ink)}
.top-band{position:absolute;left:0;top:0;width:754px;height:266px;background:linear-gradient(180deg,var(--band-top),var(--band-bottom));border-top:3px solid #e9766b}
.logo{position:absolute;left:60px;top:28px;font-family:"Libre Baskerville",serif;font-weight:700;font-size:22px;color:#fff}
.search{position:absolute;left:530px;top:37px;width:166px;height:21px;background:rgba(255,255,255,.18);font-size:7px;font-style:italic;color:#fff;padding:6px 8px}
.search svg{position:absolute;right:6px;top:4px}
.main-nav{position:absolute;left:59px;top:71px;width:636px;height:34px;background:var(--nav);display:flex;padding-left:2px}
.main-nav a{color:#fff;text-decoration:none;font-size:9.6px;line-height:34px;padding:0 11.5px;border-right:1px solid var(--nav-line)}
.main-nav a:last-child{border-right:0}
.hero{position:absolute;left:59px;top:105px;width:636px;height:239px;background:radial-gradient(circle at 70% 35%,#d65c8c,#6b2a55 45%,#2a1430);}
.hero-caption{position:absolute;left:-1px;top:117px;width:272px;height:80px;background:rgba(40,30,30,.78);color:#fff;padding:12px 19px}
.hero-caption .kicker{font-weight:300;font-size:16.5px}
.hero-caption .title{font-size:21px;line-height:1.2}
.hero-strip{position:absolute;left:0;bottom:0;width:220px;height:22px;background:rgba(0,0,0,.6);color:#fff;font-size:10.5px;line-height:22px;padding-left:9px;letter-spacing:.3px}
.hero-arrows{position:absolute;right:0;bottom:0;width:29px;height:22px;background:#222}
.intro{position:absolute;left:59px;top:362px;width:410px}
.intro h1{font-weight:400;font-size:17.5px;line-height:1.2}
.intro h1 span{font-size:13px}
.intro p{font-size:7.4px;line-height:14.3px;color:var(--muted);margin-top:8px}
.intro p + p{margin-top:3px}
.btn{position:absolute;left:60px;top:489px;width:77px;height:21px;background:var(--accent);border-radius:2px;color:#fff;font-size:7.6px;line-height:21px;text-align:center}
.video-card{position:absolute;left:483px;top:362px;width:212px;height:154px;border:1px solid var(--rule);box-shadow:0 0 4px rgba(0,0,0,.08);background:#fff}
.video{position:absolute;left:8px;top:8px;width:195px;height:137px;background:radial-gradient(circle at 55% 45%,#e8a27a,#8a3a3a 60%,#3a1a20)}
.video svg{position:absolute;left:83px;top:54px}
.rule{position:absolute;left:60px;width:635px;height:1px;background:var(--rule)}
.section-title{position:absolute;left:60px;font-size:18px;font-weight:400;color:var(--accent)}
.grid{position:absolute;left:60px;top:589px;width:636px;display:grid;grid-template-columns:repeat(5,118px);column-gap:12px;row-gap:12px}
.dest{height:129px;background:var(--card);border:1px solid #e2e2e2;box-shadow:0 1px 2px rgba(0,0,0,.08)}
.dest .photo{height:102px}
.dest .label{font-size:10px;text-align:center;line-height:26px}
.reviews{position:absolute;left:61px;top:936px;width:634px;height:124px;border:1px solid #e2e2e2;display:flex;background:linear-gradient(#fff,#f6f6f6)}
.review{flex:1;padding:14px 16px;border-right:1px solid #e2e2e2;position:relative}
.review:last-child{border-right:0}
.review h3{font-size:8.8px;font-weight:400}
.review p{font-size:7px;line-height:12px;color:var(--muted);margin-top:3px}
.avatar{position:absolute;left:16px;top:73px;width:35px;height:35px;border-radius:50%;background:#c9a58a}
.author{position:absolute;left:57px;top:75px;font-size:7.4px}
.stars{color:var(--star);font-size:9px;letter-spacing:1px;line-height:12px}
.date{font-size:7.2px;color:#aaa}
.footer{position:absolute;left:0;top:1108px;width:754px;height:92px;background:var(--footer);border-top:4px solid var(--footer-line)}
.foot-nav{position:absolute;left:59px;top:26px;font-size:8.4px;color:#fff}
.foot-nav span{color:#bbb;margin:0 4px}
.copy{position:absolute;left:59px;top:43px;font-size:8.2px;color:#aaa}
.social{position:absolute;left:615px;top:26px;display:flex;gap:3px}
.social i{width:18px;height:18px;border-radius:50%;background:#fff;display:block}
</style>
</head>
<body>
<header class="top-band">
  <div class="logo">Bride Basecamp</div>
  <div class="search">Search here..
    <svg width="12" height="12" viewBox="0 0 12 12"><circle cx="5" cy="5" r="3.8" fill="none" stroke="#fff" stroke-width="1.5"/><line x1="7.8" y1="7.8" x2="11" y2="11" stroke="#fff" stroke-width="1.6"/></svg>
  </div>
</header>
<nav class="main-nav">
  <a>HOME</a><a>ABOUT US</a><a>PACKAGES</a><a>LOCATIONS</a><a>EUROPEAN DESTINATIONS</a><a>REVIEWS</a><a>BOOKING</a><a>CONTACT</a>
</nav>
<section class="hero" role="img" aria-label="Three women laughing with cocktails on a colourful dance floor">
  <div class="hero-caption"><div class="kicker">Lorem ipsum dolor amet</div><div class="title">Pellentesque faucibus</div></div>
  <div class="hero-strip">"Part of the Peachtree Network"</div>
  <div class="hero-arrows"><svg width="29" height="22" viewBox="0 0 29 22"><path d="M12 6 8 11 12 16M17 6 21 11 17 16" fill="none" stroke="#fff" stroke-width="1.3"/></svg></div>
</section>
<section class="intro">
  <h1>Bride Basecamp - <span>hen day, night and weekend activities</span></h1>
  <p>Bride Basecamp is the place to start if you want to put together a great hen party. We have done 1000's of them over the years and know all the great places and things to do. Rather than build a big site with loads of pages that you will never read we decided lets cut to the chase and make it easy for you. All you have to do is fill out our form below and we will create a great itinerary for you.</p>
  <p>We can arrange full on hen weekends or just hen nights, just let us know a few details and we will do all the rest. We can even chase your friends for the money rather than you trying to do it</p>
</section>
<div class="btn">READ MORE</div>
<div class="video-card">
  <div class="video" role="img" aria-label="Video still of a woman singing at a party">
    <svg width="28" height="28" viewBox="0 0 28 28"><circle cx="14" cy="14" r="13" fill="#1a1a1a" stroke="#fff" stroke-width="1.5"/><path d="M11 8.5 19 14 11 19.5Z" fill="#fff"/></svg>
  </div>
</div>
<div class="rule" style="top:538px"></div>
<h2 class="section-title" style="top:554px">Booking Your Stag Do</h2>
<section class="grid">
  <div class="dest"><div class="photo" role="img" aria-label="City skyline at dusk" style="background:linear-gradient(#2f6fb8,#d48a4a)"></div><div class="label">Location/Destination</div></div>
  <div class="dest"><div class="photo" role="img" aria-label="Tower bridge over a river" style="background:linear-gradient(#e9c6d4,#7a6660)"></div><div class="label">Location/Destination</div></div>
  <div class="dest"><div class="photo" role="img" aria-label="Green limestone mountains by a river" style="background:linear-gradient(#c8d4dc,#6a8a4a)"></div><div class="label">Location/Destination</div></div>
  <div class="dest"><div class="photo" role="img" aria-label="Coastal town above a turquoise sea" style="background:linear-gradient(#8fc4de,#d9b99a 55%,#5bb3c5)"></div><div class="label">Location/Destination</div></div>
  <div class="dest"><div class="photo" role="img" aria-label="Tall glass tower against a blue sky" style="background:linear-gradient(#1f4fb5,#0e2a70)"></div><div class="label">Location/Destination</div></div>
  <div class="dest"><div class="photo" role="img" aria-label="Beach huts on a tropical shore" style="background:linear-gradient(#6aaed8,#e8dcc4)"></div><div class="label">Location/Destination</div></div>
  <div class="dest"><div class="photo" role="img" aria-label="Red pillared covered walkway" style="background:linear-gradient(90deg,#b8332c,#5a7a88,#b8332c)"></div><div class="label">Location/Destination</div></div>
  <div class="dest"><div class="photo" role="img" aria-label="Bronze statue on a dome under blue sky" style="background:linear-gradient(#3aa6e0,#3e6a6a)"></div><div class="label">Location/Destination</div></div>
  <div class="dest"><div class="photo" role="img" aria-label="Harbour bridge lit at night" style="background:linear-gradient(#1a2850,#c98a2a)"></div><div class="label">Location/Destination</div></div>
  <div class="dest"><div class="photo" role="img" aria-label="Waterfall among mossy rocks" style="background:linear-gradient(#3e4a2a,#8a9a7a)"></div><div class="label">Location/Destination</div></div>
</section>
<div class="rule" style="top:886px"></div>
<h2 class="section-title" style="top:903px">Customer Reviews</h2>
<section class="reviews">
  <article class="review"><h3>Etiam eu urna Sed porta Suspendisse</h3><p>quam leo molestie sed luctus quis feugiat in pede Fusce tellus Sed metus augue convallis et vehicula ut pulvinar eu ante Integer orci</p><div class="avatar" role="img" aria-label="Customer portrait"></div><div class="author">By Author Name<div class="stars">★★★★★</div><div class="date">on 29 November 2013</div></div></article>
  <article class="review"><h3>Etiam eu urna Sed porta Suspendisse</h3><p>quam leo molestie sed luctus quis feugiat in pede Fusce tellus Sed metus augue convallis et vehicula ut pulvinar eu ante Integer orci</p><div class="avatar" role="img" aria-label="Customer portrait"></div><div class="author">By Author Name<div class="stars">★★★★★</div><div class="date">on 29 November 2013</div></div></article>
  <article class="review"><h3>Etiam eu urna Sed porta Suspendisse</h3><p>quam leo molestie sed luctus quis feugiat in pede Fusce tellus Sed metus augue convallis et vehicula ut pulvinar eu ante Integer orci</p><div class="avatar" role="img" aria-label="Customer portrait"></div><div class="author">By Author Name<div class="stars">★★★★★</div><div class="date">on 29 November 2013</div></div></article>
</section>
<footer class="footer">
  <div class="foot-nav">HOME<span>|</span>ABOUT US<span>|</span>PACKAGES<span>|</span>LOCATIONS<span>|</span>EUROPEAN DESTINATIONS<span>|</span>REVIEWS<span>|</span>BOOKING<span>|</span>CONTACT</div>
  <div class="copy">© 2014 Company Name &nbsp;All right reserved &nbsp;Term of Use</div>
  <div class="social"><i></i><i></i><i></i><i></i></div>
</footer>
</body>
</html>
```